Full Page Ad

We are like looking for something modern, Rustic and unique for a full page ad that includes our logo, office locations, contact information. Please see our webpage and www.BRAVOClaimsteam.com. I can send our logo as well.
Updates

Looking for something elegant but industrial, rustic and modern. Added Sunday, June 4, 2017

Industry/Entity Type

Insurance

Font styles to use
Serif

Requirements
Must have
• Contact information

```html
<!DOCTYPE html>
<html lang="en">
<head>
<meta charset="utf-8">
<title>BRAVO Claims Team – Full Page Ad</title>
<link href="https://fonts.googleapis.com/css2?family=Archivo+Black&family=Oswald:wght@500;600&family=Lato:wght@400;700&display=swap" rel="stylesheet">
<style>
  :root {
    --orange: #f07a2c;
    --navy: #0f2a5e;
    --ink: #333a44;
    --paper: #f4f4f4;
    --stage: #e6e6e6;
  }
  * { margin: 0; padding: 0; box-sizing: border-box; }
  html, body { width: 1200px; height: 1200px; overflow: hidden; background: var(--stage); }
  .ad {
    position: absolute; left: 185px; top: 19px;
    width: 918px; height: 1285px;
    transform: scale(0.9043); transform-origin: top left;
    background: var(--paper); overflow: hidden;
    box-shadow: 0 6px 24px rgba(0,0,0,.18);
  }
  .ad__art { position: absolute; inset: 0; }
  .brand { position: absolute; left: 0; right: 0; top: 505px; text-align: center; }
  .brand__name {
    font-family: "Archivo Black", sans-serif; font-size: 104px; line-height: 1;
    color: var(--orange); letter-spacing: 2px;
  }
  .brand__full {
    font-family: "Lato", sans-serif; font-size: 19px; color: var(--navy);
    letter-spacing: .5px; margin-top: 12px;
  }
  .headline {
    position: absolute; left: 0; right: 0; top: 632px; text-align: center;
    font-family: "Oswald", sans-serif; font-weight: 600; font-size: 82px; line-height: 1;
    color: var(--orange); letter-spacing: -2px; transform: scaleX(.86);
  }
  .tagline {
    position: absolute; left: 0; right: 0; top: 717px; text-align: center;
    font-family: "Lato", sans-serif; font-size: 19px; color: var(--navy);
  }
  .offices {
    position: absolute; left: 38px; top: 764px; width: 850px;
    display: grid; grid-template-columns: repeat(4, 200px); column-gap: 16px;
    grid-auto-rows: 140px;
  }
  .office__city {
    height: 28px; border-radius: 14px; background: var(--navy); color: #fff;
    font-family: "Oswald", sans-serif; font-weight: 500; font-size: 16px;
    line-height: 28px; text-align: center; text-transform: uppercase; margin-bottom: 6px;
  }
  .office__line {
    position: relative; padding-left: 22px;
    font-family: "Lato", sans-serif; font-size: 15px; line-height: 18px; color: var(--ink);
  }
  .office__phone { margin-top: 8px; }
  .office__line svg { position: absolute; left: 6px; top: 2px; width: 10px; height: 13px; fill: var(--ink); }
  .hotline {
    position: absolute; left: 0; right: 0; top: 1183px; height: 70px;
    background: var(--navy); color: #fff; text-align: center;
    font-family: "Lato", sans-serif; font-size: 58px; line-height: 70px;
  }
</style>
</head>
<body>
<svg width="0" height="0" style="position:absolute">
  <symbol id="pin" viewBox="0 0 10 13"><path d="M5 0a4.5 4.5 0 0 0-4.5 4.5C.5 8 5 13 5 13s4.5-5 4.5-8.5A4.5 4.5 0 0 0 5 0zm0 6.3a1.8 1.8 0 1 1 0-3.6 1.8 1.8 0 0 1 0 3.6z"/></symbol>
  <symbol id="phone" viewBox="0 0 10 13"><circle cx="5" cy="6.5" r="4.3" fill="none" stroke="#333a44" stroke-width="1"/><path d="M3.4 4.2l1 1-.5.6c.3.7.8 1.2 1.5 1.5l.6-.5 1 1-.7.8C4.6 8.4 3 6.8 2.8 5z"/></symbol>
</svg>

<main class="ad">
  <svg class="ad__art" viewBox="0 0 918 1285" preserveAspectRatio="none">
    <defs>
      <radialGradient id="fire" cx="0.3" cy="0.35" r="0.8">
        <stop offset="0" stop-color="#ffb060"/>
        <stop offset=".45" stop-color="#e0692a"/>
        <stop offset="1" stop-color="#7a3418"/>
      </radialGradient>
      <linearGradient id="flood" x1="0" y1="0" x2="0" y2="1">
        <stop offset="0" stop-color="#4a4a4a"/>
        <stop offset="1" stop-color="#2c2c2c"/>
      </linearGradient>
    </defs>
    <rect width="918" height="520" fill="url(#fire)" role="img" aria-label="Photo of a firefighter spraying water into a burning house"/>
    <path d="M0,500 C380,480 720,310 918,120 L918,700 L0,700 Z" fill="url(#flood)" role="img" aria-label="Photo of a flooded street with houses and a speed limit sign"/>
    <path d="M0,478 C360,470 700,300 918,40" fill="none" stroke="var(--navy)" stroke-width="26"/>
    <path d="M0,494 C380,484 730,330 918,150" fill="none" stroke="var(--orange)" stroke-width="12"/>
    <path d="M0,466 C260,450 520,430 700,500 C800,545 870,620 918,690" fill="none" stroke="var(--orange)" stroke-width="28"/>
    <path d="M0,476 C260,460 520,440 700,510 C800,555 870,630 918,700 L918,1285 L0,1285 Z" fill="var(--paper)"/>
  </svg>

  <header class="brand">
    <div class="brand__name">BRAVO</div>
    <div class="brand__full">BRAVO CLAIMS TEAM SERVICES</div>
  </header>
  <h1 class="headline">WHEN IT HAPPENS</h1>
  <p class="tagline">Accidents, Disasters, Fire, Flood, Wind, Property &amp; Liability</p>

  <section class="offices">
    <article class="office">
      <h2 class="office__city">Albany, NY – Home Office</h2>
      <p class="office__line"><svg><use href="#pin"/></svg>PO Box 218<br>410 Birchwood Road<br>Clifton Park, NY 12065</p>
      <p class="office__line office__phone"><svg><use href="#phone"/></svg>518-555-0102</p>
    </article>
    <article class="office">
      <h2 class="office__city">Utica, NY</h2>
      <p class="office__line"><svg><use href="#pin"/></svg>PO Box 3310, Utica, NY 13501<br>22 Maple Turnpike Suite 4<br>New Hartford, NY 13413</p>
      <p class="office__line office__phone"><svg><use href="#phone"/></svg>315-555-0167</p>
    </article>
    <article class="office">
      <h2 class="office__city">Plattsburgh, NY</h2>
      <p class="office__line"><svg><use href="#pin"/></svg>P.O. Box 1190<br>Plattsburgh, NY 12901</p>
      <p class="office__line office__phone" style="margin-top:26px"><svg><use href="#phone"/></svg>518-555-0102</p>
    </article>
    <article class="office">
      <h2 class="office__city">Poughkeepsie, NY</h2>
      <p class="office__line"><svg><use href="#pin"/></svg>8 Harbor Light Rd<br>Poughkeepsie, NY 12601</p>
      <p class="office__line office__phone" style="margin-top:26px"><svg><use href="#phone"/></svg>845-555-0150</p>
    </article>

    <article class="office">
      <h2 class="office__city">Queensbury, NY</h2>
      <p class="office__line"><svg><use href="#pin"/></svg>17 Pinecrest Lane<br>Queensbury, NY 12804</p>
      <p class="office__line office__phone" style="margin-top:26px"><svg><use href="#phone"/></svg>518-555-0102</p>
    </article>
    <article class="office">
      <h2 class="office__city">Rochester, NY</h2>
      <p class="office__line"><svg><use href="#pin"/></svg>880 Fairmont Road<br>Suite 310B<br>Rochester, NY 14624</p>
      <p class="office__line office__phone"><svg><use href="#phone"/></svg>585-555-0170</p>
    </article>
    <article class="office">
      <h2 class="office__city">Syracuse, NY</h2>
      <p class="office__line"><svg><use href="#pin"/></svg>PO Box 5120<br>742 Linden Street<br>Syracuse, NY 13217</p>
      <p class="office__line office__phone"><svg><use href="#phone"/></svg>315-555-0168</p>
    </article>
    <article class="office">
      <h2 class="office__city">Watertown, NY</h2>
      <p class="office__line"><svg><use href="#pin"/></svg>P.O. Box 76<br>Watertown, NY 13601</p>
      <p class="office__line office__phone" style="margin-top:26px"><svg><use href="#phone"/></svg>315-555-0168</p>
    </article>

    <article class="office">
      <h2 class="office__city">Elmira, NY</h2>
      <p class="office__line"><svg><use href="#pin"/></svg>P.O. Box 309<br>Horseheads, NY 14845</p>
      <p class="office__line office__phone"><svg><use href="#phone"/></svg>607-555-0140</p>
    </article>
    <article class="office">
      <h2 class="office__city">Buffalo, NY</h2>
      <p class="office__line"><svg><use href="#pin"/></svg>55 Lakeview Street, Suite 208<br>Buffalo, NY 14202</p>
      <p class="office__line office__phone"><svg><use href="#phone"/></svg>1-800-555-0148</p>
    </article>
    <article class="office">
      <h2 class="office__city">Long Island, NY</h2>
      <p class="office__line"><svg><use href="#pin"/></svg>P.O. Box 611<br>Rockville Centre,<br>NY 11570</p>
      <p class="office__line" style="margin-top:2px"><svg><use href="#phone"/></svg>1-800-555-0148</p>
    </article>
    <article class="office">
      <h2 class="office__city">Springfield, MA</h2>
      <p class="office__line"><svg><use href="#pin"/></svg>P.O. Box 2270<br>88 Walnut St, Ste 2B<br>Springfield, MA 01103</p>
      <p class="office__line office__phone"><svg><use href="#phone"/></svg>413-555-0130</p>
    </article>
  </section>

  <footer class="hotline">1-800-555-0148</footer>
</main>
</body>
</html>
```